mothers day ad for martial arts school

I am looking to have a nice flyer/handout to promote my martial arts school. It is for our promotion of "mom's train free" for mothers day in May. I would like an ad that would inspire a mother to learn self defense and to improve their fitness. It can have pictures but not necessarily a requirement. Pictures don't have to be of a lady in a martial arts uniform. It may be better if they are not. It also doesn't have to be standard sheet of paper size, as these are going to be handouts the size can be smaller. I would like our Crane Hollow logo on the flyer.

Target Market(s)

mothers that hadn't thought about martial arts before but would be convinced to try it

Industry/Entity Type

School

Requirements
Must have
• text, photos that would appeal to and encourage a mother to try a self defense/fitness class
Nice to have
• our logo and text and possibly pictures that would inspire a mother to join a martial arts class

```html
<!DOCTYPE html>
<html lang="en">
<head>
<meta charset="utf-8">
<title>Crane Hollow Martial Arts – Mom's Train Free</title>
<link rel="stylesheet" href="https://fonts.googleapis.com/css2?family=Great+Vibes&family=Alegreya:wght@400&family=Roboto+Condensed:wght@700&family=Open+Sans:wght@600;700&family=Ubuntu:wght@400&family=Russo+One&family=Roboto:ital,wght@0,700;1,400&display=swap">
<style>
  :root {
    --ink: #050708;
    --teal: #0f4a44;
    --teal-deep: #0a2e2c;
    --brand-red: #e3202b;
    --script-red: #e0222c;
    --body-yellow: #ecde6a;
    --web-yellow: #f0e46a;
    --white: #ffffff;
    --lime: #a8d62c;
    --green: #2fa83c;
    --sky: #1a8fd0;
    --silver: #b9c3c6;
  }
  html, body {
    margin: 0;
    padding: 0;
    width: 1200px;
    height: 822px;
    overflow: hidden;
    background: #2a2a2a;
  }
  .flyer {
    position: relative;
    width: 1200px;
    height: 822px;
    overflow: hidden;
    background:
      radial-gradient(ellipse 520px 420px at 640px 120px, var(--teal) 0%, rgba(15,74,68,0.55) 45%, rgba(5,7,8,0) 100%),
      linear-gradient(90deg, var(--ink) 0%, var(--ink) 30%, var(--teal-deep) 60%, var(--teal) 100%);
    font-family: "Open Sans", sans-serif;
  }
  .artwork {
    position: absolute;
    inset: 0;
  }
  .brand {
    position: absolute;
    left: 36px;
    top: 62px;
    display: flex;
    align-items: center;
    gap: 14px;
  }
  .brand-dot {
    width: 52px;
    height: 52px;
    border-radius: 50%;
    background: var(--brand-red);
  }
  .brand-name {
    font-family: "Open Sans", sans-serif;
    font-weight: 700;
    font-size: 40px;
    color: var(--white);
    letter-spacing: 0.5px;
    line-height: 1;
  }
  .occasion {
    position: absolute;
    left: 36px;
    top: 196px;
    font-family: "Great Vibes", cursive;
    font-size: 50px;
    color: var(--script-red);
    line-height: 1;
  }
  .intro {
    position: absolute;
    left: 33px;
    top: 322px;
    width: 296px;
    margin: 0;
    font-family: "Alegreya", serif;
    font-size: 15.5px;
    line-height: 24.8px;
    color: var(--body-yellow);
    text-align: justify;
  }
  .contact {
    position: absolute;
    left: 33px;
    top: 624px;
    width: 400px;
  }
  .contact-lead {
    margin: 0 0 0 4px;
    font-size: 21px;
    font-weight: 600;
    color: var(--white);
    line-height: 1.2;
  }
  .contact-phone {
    margin: 2px 0 0 0;
    font-family: "Roboto Condensed", sans-serif;
    font-weight: 700;
    font-size: 50px;
    color: var(--brand-red);
    line-height: 1.05;
  }
  .contact-rule {
    width: 342px;
    height: 1px;
    margin: 8px 0 10px;
    background: #7d8a3a;
  }
  .contact-note {
    margin: 0;
    font-family: "Roboto", sans-serif;
    font-style: italic;
    font-size: 16px;
    color: var(--white);
  }
  .contact-web {
    margin: 6px 0 0 0;
    font-weight: 700;
    font-size: 29px;
    letter-spacing: 0.6px;
    color: var(--web-yellow);
    line-height: 1.2;
  }
  .offer-badge {
    position: absolute;
    left: 432px;
    top: 157px;
    width: 256px;
    height: 256px;
    border-radius: 50%;
    background: radial-gradient(circle at 45% 30%, #8fd64a 0%, var(--green) 45%, var(--lime) 100%);
    box-shadow: 0 0 0 3px rgba(255,255,255,0.25), 0 6px 18px rgba(0,0,0,0.45);
    display: flex;
    flex-direction: column;
    align-items: center;
    justify-content: center;
    font-family: "Roboto Condensed", sans-serif;
    font-weight: 700;
    font-size: 58px;
    line-height: 0.98;
    color: var(--white);
    text-shadow: 0 3px 5px rgba(0,0,0,0.45);
    text-align: center;
  }
  .tagline {
    position: absolute;
    left: 560px;
    top: 578px;
    width: 210px;
    margin: 0;
    font-family: "Ubuntu", sans-serif;
    font-size: 31px;
    line-height: 41px;
    color: var(--white);
    text-align: center;
  }
  .facility {
    position: absolute;
    right: 48px;
    top: 734px;
    margin: 0;
    font-family: "Russo One", sans-serif;
    font-size: 25px;
    line-height: 31px;
    color: var(--white);
    text-align: right;
  }
</style>
</head>
<body>
<main class="flyer">
  <svg class="artwork" width="1200" height="822" viewBox="0 0 1200 822" aria-hidden="false">
    <defs>
      <linearGradient id="photoTone" x1="0" y1="0" x2="1" y2="1">
        <stop offset="0" stop-color="#1c1614"/>
        <stop offset="0.45" stop-color="#5a3a30"/>
        <stop offset="0.7" stop-color="#c39886"/>
        <stop offset="1" stop-color="#d9c3ae"/>
      </linearGradient>
      <linearGradient id="skyBand" x1="0" y1="1" x2="1" y2="0">
        <stop offset="0" stop-color="#0e6f9e"/>
        <stop offset="1" stop-color="var(--sky)"/>
      </linearGradient>
    </defs>
    <path class="photo-area" role="img" aria-label="Photograph of a young woman with dark wavy hair holding an open hand in a martial arts guard pose"
      fill="url(#photoTone)"
      d="M 760 160 Q 950 140 1200 110 L 1200 822 L 720 822 A 395 395 0 0 1 760 160 Z"/>
    <path class="top-wave" fill="var(--teal)" opacity="0.9"
      d="M 650 150 Q 760 40 900 60 Q 1000 75 1060 150 Q 1130 150 1200 120 L 1200 0 L 650 0 Z"/>
    <path class="sky-band" fill="url(#skyBand)"
      d="M 700 822 Q 900 740 1000 700 Q 1100 665 1200 660 L 1200 822 Z"/>
    <g class="swoosh-lines" fill="none" stroke="var(--silver)" stroke-width="1.4">
      <path d="M 720 822 A 398 398 0 0 1 700 100"/>
      <path d="M 740 818 A 410 410 0 0 1 690 120" opacity="0.7"/>
      <path d="M 440 360 Q 470 600 700 780 Q 840 830 1000 790" opacity="0.8"/>
      <path d="M 660 110 Q 800 40 960 70 Q 1050 95 1090 160" opacity="0.8"/>
      <path d="M 670 125 Q 810 55 965 85 Q 1050 110 1085 170" opacity="0.6"/>
      <path d="M 900 730 Q 1050 670 1200 670" opacity="0.9"/>
      <path d="M 905 740 Q 1055 682 1200 680" opacity="0.6"/>
    </g>
  </svg>

  <header class="brand">
    <span class="brand-dot" aria-hidden="true"></span>
    <span class="brand-name">Crane Hollow Martial Arts</span>
  </header>

  <p class="occasion">for mothers day in May</p>

  <p class="intro">Lorem ipsum dolor sit amet, consectetur adipiscing elit, sed do eiusmod tempor incididunt ut labore et dolore magna aliqua. Ut enim ad minim veniam, quis nostrud exercitation ullamco laboris nisi ut aliquip ex ea commodo consequat. Duis aute irure dolor in reprehenderit in voluptate velit esse cillum dolore eu fugiat nulla pariatur. Duis aute irure dolor in reprehenderit in voluptate velit esse cillum dolore eu fugiat nulla pariatur.</p>

  <section class="contact">
    <p class="contact-lead">Mother to learn self defense</p>
    <p class="contact-phone">(555) 014-2290</p>
    <div class="contact-rule"></div>
    <p class="contact-note">For more information please contact us at</p>
    <p class="contact-web">cranehollowmartialarts.com</p>
  </section>

  <div class="offer-badge">
    <span>MOM'S</span>
    <span>TRAIN</span>
    <span>FREE</span>
  </div>

  <p class="tagline">Learn Life Skills Through Martial Arts</p>

  <p class="facility">ALL-DAY<br>FITNESS CENTER</p>
</main>
</body>
</html>
```